Business cards for Harbourline Supply Pty Ltd that import building products into Australia from China
Target Market(s)
Business to Business
Industry/Entity Type
Business
Contact Information for Business Card
Front: Logo and Business Name
Rear:
Vernon Ashcombe
General Manager
Mobile: 0427 619 354
email: vern@harbourlinesupply.com.au
alternative email: vern@coastwardgoods.com.au
web: www.harbourlinesupply.com.au
Adelaide, Brisbane and Darwin
Colors
ec1f27
fbee3d

```html
<!DOCTYPE html>
<html lang="en">
<head>
<meta charset="utf-8">
<title>Harbourline Supply – Business Cards</title>
<link rel="stylesheet" href="https://fonts.googleapis.com/css2?family=Arimo:wght@400&display=swap">
<style>
  :root {
    --brand-red: #ec1f27;
    --brand-yellow: #fbee3d;
    --card-yellow: #ffe000;
    --card-red: #e31b23;
    --ink: #1a1a1a;
    --backdrop: #5a3b2c;
    --ghost: rgba(255, 255, 255, 0.07);
    --icon-mark: #ffffff;
  }
  * { box-sizing: border-box; margin: 0; padding: 0; }
  html, body {
    width: 1200px; height: 448px; overflow: hidden;
    background: var(--backdrop);
    font-family: "Arimo", Arial, sans-serif;
  }
  .stage { position: relative; width: 1200px; height: 448px; }
  .card {
    position: absolute; top: 66px; width: 556px; height: 316px;
    overflow: hidden;
  }

  /* Contact side */
  .card--contact { left: 29px; background: var(--card-yellow); }
  .card--contact .wordmark {
    position: absolute; left: 26px; top: 112px;
    color: var(--brand-red); font-size: 36px; line-height: 35px;
    letter-spacing: -1px;
  }
  .divider {
    position: absolute; left: 229px; top: 32px;
    width: 2px; height: 252px; background: var(--brand-red);
  }
  .person { position: absolute; left: 246px; top: 44px; }
  .person__name { font-size: 22px; color: var(--ink); line-height: 27px; }
  .person__role { font-size: 12px; color: var(--brand-red); text-transform: uppercase; margin-top: 1px; }
  .contact-row {
    position: absolute; left: 246px; display: flex; align-items: flex-start; gap: 10px;
    font-size: 16px; color: var(--ink); line-height: 21px;
  }
  .contact-row svg { flex: none; width: 20px; height: 20px; }
  .contact-row--mobile { top: 141px; }
  .contact-row--email { top: 196px; }
  .contact-row--web { top: 259px; }

  /* Logo side */
  .card--brand { left: 604px; background: var(--card-red); }
  .ghost-word {
    position: absolute; color: var(--ghost); font-size: 136px; line-height: 1;
    white-space: nowrap; letter-spacing: -2px;
  }
  .ghost-word--top { left: -2px; top: -8px; }
  .ghost-word--bottom { left: 150px; top: 112px; }
  .card--brand .wordmark {
    position: absolute; left: 0; right: 0; top: 86px; text-align: center;
    color: var(--card-yellow); font-size: 66px; line-height: 64px; letter-spacing: -1px;
  }
</style>
</head>
<body>
<main class="stage">
  <section class="card card--contact" aria-label="Business card, contact side">
    <div class="wordmark">harbourline<br>supply</div>
    <div class="divider"></div>
    <div class="person">
      <p class="person__name">Vernon Ashcombe</p>
      <p class="person__role">General Manager</p>
    </div>
    <div class="contact-row contact-row--mobile">
      <svg viewBox="0 0 20 20" aria-hidden="true">
        <circle cx="10" cy="10" r="10" fill="var(--brand-red)"/>
        <rect x="7" y="4.5" width="6" height="11" rx="1.2" fill="none" stroke="var(--icon-mark)" stroke-width="1.4"/>
        <circle cx="10" cy="13.3" r="0.8" fill="var(--icon-mark)"/>
      </svg>
      <span>0427 619 354</span>
    </div>
    <div class="contact-row contact-row--email">
      <svg viewBox="0 0 20 20" aria-hidden="true">
        <circle cx="10" cy="10" r="10" fill="var(--brand-red)"/>
        <rect x="5" y="6.5" width="10" height="7" rx="1" fill="var(--icon-mark)"/>
        <path d="M5.3 7 L10 10.6 L14.7 7" fill="none" stroke="var(--brand-red)" stroke-width="1.2"/>
      </svg>
      <span>vern@harbourlinesupply.com.au<br>vern@coastwardgoods.com.au</span>
    </div>
    <div class="contact-row contact-row--web">
      <svg viewBox="0 0 20 20" aria-hidden="true">
        <circle cx="10" cy="10" r="10" fill="var(--brand-red)"/>
        <g fill="none" stroke="var(--icon-mark)" stroke-width="1.1">
          <circle cx="10" cy="10" r="5"/>
          <ellipse cx="10" cy="10" rx="2.2" ry="5"/>
          <path d="M5 10 H15 M6 7.5 H14 M6 12.5 H14"/>
        </g>
      </svg>
      <span>www.harbourlinesupply.com.au</span>
    </div>
  </section>

  <section class="card card--brand" aria-label="Business card, brand side">
    <div class="ghost-word ghost-word--top" aria-hidden="true">harbour</div>
    <div class="ghost-word ghost-word--bottom" aria-hidden="true">supply</div>
    <div class="wordmark">harbourline<br>supply</div>
  </section>
</main>
</body>
</html>
```